Website design for Meridale Transfers

We need a website design based upon the Meridale Transfers look-and-feel. Meridale Transfers is all about connecting in the dynamic and fast moving world of (internet and mobile) payments. Our logo and colors (dark blue, grey and white) reflect this. The font we use is " Museo". See attached files. Our website needs to be responsive to the screen of the device used. Preferably based upon the wordpress theme, which supports many widgets and is open source:
http://layoutbazaar.example/item/solo-adaptive-scrolling-site-template/8316470. Please share your thoughts, suggestions and proposal and let me know what you need me to do or share with you to make this happen. Thanks. Wouter.

```html
<!DOCTYPE html>
<html lang="en">
<head>
<meta charset="utf-8">
<title>Meridale Transfers</title>
<link rel="stylesheet" href="https://fonts.googleapis.com/css2?family=Open+Sans:ital,wght@0,300;0,400;0,600;1,400&display=swap">
<style>
:root{
  --navy:#0c2b5e;
  --navy-deep:#09214a;
  --navy-active:#1d3d70;
  --blue-text:#1c3d73;
  --ink:#333;
  --body:#555;
  --muted:#888;
  --line:#d6d6d6;
  --band:#e4e4e4;
  --band-light:#ececec;
  --white:#fff;
}
*{box-sizing:border-box;margin:0;padding:0}
html,body{width:1200px;height:3315px;overflow:hidden}
body{font-family:"Open Sans",Arial,sans-serif;color:var(--body);background:var(--white);position:relative}
.section{position:absolute;left:0;width:1200px}
.abs{position:absolute}

/* hero */
.hero{top:0;height:464px;background:linear-gradient(100deg,#8f8a86 0%,#a9b3bf 30%,#9cb4d6 55%,#8ea0c8 75%,#c07c86 100%);overflow:hidden}
.hero-photo{position:absolute;inset:0;background:radial-gradient(ellipse 420px 260px at 420px 180px,rgba(235,225,215,.55),transparent 70%),radial-gradient(ellipse 300px 200px at 1100px 120px,rgba(190,70,80,.45),transparent 70%)}
.brand{position:absolute;display:flex;flex-direction:column;align-items:center;color:var(--white);font-weight:400}
.brand-mark{width:34px;height:34px;border:2px solid var(--white);margin-bottom:6px}
.hero .brand{left:50px;top:22px;font-size:18px}
.hero-title{position:absolute;top:262px;left:0;width:1200px;text-align:center;color:var(--white);font-weight:300;font-size:30px;letter-spacing:1px;text-transform:uppercase}
.hero-sub{position:absolute;top:304px;left:0;width:1200px;text-align:center;color:var(--white);font-size:13px;line-height:18px}
.btn-more{position:absolute;left:544px;top:360px;width:114px;height:34px;background:rgba(120,130,140,.75);color:var(--white);font-size:12px;font-weight:600;line-height:34px;text-align:center}
.dots{position:absolute;left:1158px;top:234px;display:flex;flex-direction:column;gap:7px}
.dots span{width:11px;height:11px;border:2px solid var(--white);border-radius:50%}
.dots span.on{background:var(--white)}

/* nav */
.nav{top:464px;height:62px;background:var(--navy)}
.nav .brand{left:52px;top:8px;font-size:12px}
.nav .brand-mark{width:24px;height:24px;margin-bottom:4px}
.menu{position:absolute;left:354px;top:0;display:flex;height:62px}
.menu a{color:var(--white);text-decoration:none;font-size:13px;line-height:62px;padding:0 19px}
.menu a.active{background:var(--navy-active)}
.search{position:absolute;left:1127px;top:22px}

/* ways */
.ways{top:526px;height:612px}
.h-section{color:var(--blue-text);font-weight:400;font-size:27px}
.ways .h-section{position:absolute;top:62px;width:1200px;text-align:center}
.intro{position:absolute;left:165px;width:875px;text-align:center;font-size:12.5px;line-height:17px;color:var(--body)}
.feature{position:absolute;top:300px;width:250px;text-align:center}
.feature h3{font-weight:400;font-size:22px;color:var(--blue-text)}
.feature svg{display:block;margin:22px auto 0}
.feature p{margin-top:34px;font-size:12.5px;line-height:17px}
.feature .more{display:block;margin-top:12px;font-style:italic;font-size:12px;color:var(--blue-text);font-weight:600}

/* payment page */
.payment{top:1138px;height:597px;background:linear-gradient(160deg,#e9e9e9,#dcdcdc 60%,#e6e6e6);overflow:hidden}
.payment .h-section{position:absolute;top:52px;width:1200px;text-align:center;font-size:27px}
.payment .lead{position:absolute;top:92px;width:1200px;text-align:center;font-size:12.5px}
.product-name{position:absolute;left:155px;top:200px;font-size:28px;font-weight:400;color:var(--ink)}
.product-copy{position:absolute;left:155px;top:248px;width:480px;font-size:12.5px;line-height:16px}
.pager{position:absolute;left:155px;top:453px;display:flex;gap:3px;align-items:center}
.pager span{width:49px;height:44px;background:var(--navy);display:flex;align-items:center;justify-content:center}
.pager em{font-style:normal;font-size:13px;color:var(--blue-text);margin-left:20px}
.laptop-screen{position:absolute;left:688px;top:130px;width:512px;height:372px;border-radius:18px 0 0 0;background:linear-gradient(180deg,#c9cbce,#eef0f2 40%,#d5d7da)}
.laptop-base{position:absolute;left:580px;top:500px;width:620px;height:16px;border-radius:0 0 0 40px;background:linear-gradient(180deg,#d8dadc,#a9acb0)}

/* testimonials */
.testimonials{top:1735px;height:497px}
.testimonials h2{position:absolute;left:210px;width:366px;top:30px;text-align:center;font-weight:400;font-size:28px;color:var(--ink)}
.video{position:absolute;left:197px;top:82px;width:395px;height:234px;background:linear-gradient(110deg,#9fb0b4,#c8c2ba 50%,#8b8076)}
.play{position:absolute;left:163px;top:83px;width:68px;height:68px;border:3px solid var(--white);border-radius:50%;background:rgba(255,255,255,.25)}
.play::after{content:"";position:absolute;left:25px;top:17px;border-left:24px solid var(--white);border-top:14px solid transparent;border-bottom:14px solid transparent}
.chev{position:absolute;top:206px}
.quote{position:absolute;left:180px;top:343px;width:430px;text-align:center;font-size:13px;line-height:18px}
.who{position:absolute;left:180px;top:413px;width:430px;text-align:center;font-size:13px;line-height:18px}
.who strong{color:var(--ink);font-weight:600}
.fan{position:absolute;left:745px;top:80px;width:342px}
.fan-head{display:flex;gap:10px;align-items:center}
.fan-sq{width:48px;height:48px;background:var(--navy)}
.fan-head b{display:block;font-weight:400;font-size:22px;color:var(--ink);line-height:24px}
.fan-head span{font-size:12px}
.fan-box{margin-top:14px;border-bottom:1px solid var(--line);padding-bottom:10px}
.fan-row{display:flex;align-items:center;gap:10px;font-size:12px;color:var(--navy);font-weight:600;margin-top:14px}
.fan-like{background:var(--navy-active);color:var(--white);font-size:11px;padding:2px 8px;margin-left:auto}
.fan-count{font-size:11px;margin:8px 0 6px 17px}
.fan-grid{margin-left:17px;width:321px;height:148px;background:repeating-linear-gradient(90deg,#8a8580 0 42px,#fff 42px 45px),#8a8580}
.fan-foot{font-size:10px;margin-top:8px}

/* contact */
.contact{top:2232px;height:111px;background:var(--band-light)}
.contact h2{position:absolute;top:20px;width:1200px;text-align:center;font-weight:400;font-size:22px;color:var(--blue-text)}
.contact p{position:absolute;top:52px;left:210px;width:780px;text-align:center;font-size:12.5px;line-height:18px}
.map{top:2343px;height:597px;background:linear-gradient(135deg,#dcdcdc,#cfcfcf 50%,#e0e0e0)}
.zoom{position:absolute;left:55px;width:49px;height:51px;background:var(--navy);color:var(--white);font-size:28px;font-weight:300;text-align:center;line-height:48px}

/* clients */
.clients{top:2940px;height:154px;border-top:1px solid var(--line)}
.clients h3{position:absolute;top:-1px;width:1200px;text-align:center;font-weight:400;font-size:17px;color:var(--blue-text)}
.clients h3 span{background:var(--white);padding:0 14px}
.client-row{position:absolute;left:0;top:30px;width:1200px;height:110px;display:flex}
.client{flex:1;display:flex;align-items:center;justify-content:center;font-size:21px;color:#7a7a7a;border-left:1px solid var(--line)}
.client:first-child{border-left:none}

/* footer */
.footer{top:3094px;height:221px;background:var(--navy-deep);color:var(--white)}
.fcol{position:absolute;top:38px}
.fcol h4{font-size:15px;font-weight:600;margin-bottom:10px}
.fcol li{list-style:none;font-size:11.5px;line-height:14px;color:#b7c3d8;text-transform:uppercase}
.social{display:flex;gap:9px;margin-top:10px}
.social span{width:28px;height:28px;border-radius:50%;background:#2b8ad8}
.news h4{font-weight:400;font-size:18px}
.news form{display:flex;margin-top:4px}
.news input{width:237px;height:35px;border:0;padding:0 12px;font-family:inherit;font-size:12px;font-style:italic;color:#999}
.news button{width:97px;height:35px;border:0;background:#4d5360;color:var(--white);font-family:inherit;font-size:16px}
.copy{position:absolute;right:102px;top:186px;font-size:10.5px;color:#8ea0c0;text-transform:uppercase}
</style>
</head>
<body>

<section class="section hero">
  <div class="hero-photo" role="img" aria-label="Blurred photo of a hand holding a smartphone"></div>
  <div class="brand"><span class="brand-mark"></span>Meridale Transfers</div>
  <h1 class="hero-title">Are you looking for a payment gateway?</h1>
  <p class="hero-sub">Sed tortor diam, condimentum non ligula Duis semper vestibulum Donec quis rhoncus tortor,<br>vel scelerisque quam. Nam in arcu odio</p>
  <a class="btn-more">KNOW MORE</a>
  <div class="dots"><span class="on"></span><span></span><span></span></div>
</section>

<nav class="section nav">
  <div class="brand"><span class="brand-mark"></span>Meridale Transfers</div>
  <div class="menu">
    <a class="active">HOME</a><a>ABOUT US</a><a>SERVICES</a><a>GALLERY</a><a>BLOG</a><a>TESTIMONIALS</a><a>CONTACT US</a><a>LOGIN</a>
  </div>
  <svg class="search" width="18" height="18" viewBox="0 0 18 18"><circle cx="7" cy="7" r="5" fill="none" stroke="#fff" stroke-width="2"/><path d="M11 11l5 5" stroke="#fff" stroke-width="2.4"/></svg>
</nav>

<section class="section ways">
  <h2 class="h-section">Accept Payment Through Many ways</h2>
  <p class="intro" style="top:137px">Praesent varius elit pellentesque arcu molestie condimentum. Suspendisse potenti. Fusce a pharetra arcu, eget aliquam leo. Maecenas sodales sagittis sollicitudin. Nunc semper, ligula non fermentum scelerisque, est mauris pharetra arcu, vitae venenatis eros odio et odio. Aliquam mollis mi a ornare congue. Ut vel purus fermentum, accumsan orci ullamcorper, ullamcorper tortor. Nulla ac laoreet elit, a fringilla turpis. Nunc tristique sollicitudin ante at tempus. Curabitur mattis magna sapien, ac porttitor elit venenatis vel.</p>
  <p class="intro" style="top:213px">Nulla in euismod tortor. Suspendisse potenti. Curabitur faucibus at urna sit amet tincidunt.</p>

  <div class="feature" style="left:145px">
    <h3>Easiest way</h3>
    <svg width="100" height="90" viewBox="0 0 100 90"><rect x="4" y="14" width="66" height="46" rx="3" fill="none" stroke="#222" stroke-width="6"/><rect x="22" y="64" width="30" height="6" fill="#222"/><rect x="14" y="72" width="46" height="6" fill="#222"/><rect x="66" y="4" width="30" height="74" rx="4" fill="#fff" stroke="#222" stroke-width="6"/><circle cx="81" cy="70" r="2.5" fill="#222"/></svg>
    <p>Morbi placerat neque tortor, eget posuere velit eleifend in. Sed tortor diam, condimentum non ligula at, dapibus egestas nibh.</p>
    <span class="more">Read more</span>
  </div>
  <div class="feature" style="left:476px">
    <h3>Free to sign up</h3>
    <svg width="110" height="90" viewBox="0 0 110 90"><circle cx="28" cy="30" r="13" fill="#222"/><circle cx="82" cy="30" r="13" fill="#222"/><path d="M4 78c0-18 10-28 24-28s22 8 24 20v8z M58 78v-8c2-12 10-20 24-20s24 10 24 28z" fill="#222"/><circle cx="55" cy="24" r="17" stroke="#fff" stroke-width="4" fill="#222"/><path d="M22 86c0-24 14-38 33-38s33 14 33 38z" fill="#222" stroke="#fff" stroke-width="4"/></svg>
    <p>Morbi placerat neque tortor, eget posuere velit eleifend in. Sed tortor diam, condimentum non ligula at, dapibus egestas nibh.</p>
    <span class="more">Read more</span>
  </div>
  <div class="feature" style="left:805px">
    <h3>Strong protection</h3>
    <svg width="60" height="90" viewBox="0 0 60 90"><path d="M14 42V28a16 16 0 0 1 32 0v14" fill="none" stroke="#222" stroke-width="7"/><rect x="6" y="40" width="48" height="42" rx="4" fill="#222"/><circle cx="30" cy="58" r="5" fill="#fff"/><rect x="28" y="60" width="4" height="12" fill="#fff"/></svg>
    <p>Morbi placerat neque tortor, eget posuere velit eleifend in. Sed tortor diam, condimentum non ligula at, dapibus egestas nibh.</p>
    <span class="more">Read more</span>
  </div>
</section>

<section class="section payment">
  <h2 class="h-section">Payment Page</h2>
  <p class="lead">Neque porro quisquam est qui dolorem ipsum quia dolor sit amet, consectetur, adipisci velit</p>
  <div class="laptop-screen" role="img" aria-label="Laptop showing a sample shipping and payment checkout page"></div>
  <div class="laptop-base"></div>
  <h3 class="product-name">Mujanio Applicano</h3>
  <div class="product-copy">
    <p>Praesent varius elit pellentesque arcu molestie condimentum. Suspendisse potenti. Fusce a pharetra arcu, eget aliquam leo. Maecenas sodales sagittis sollicitudin. Nunc semper, ligula non fermentum scelerisque, est mauris pharetra arcu, vitae venenatis eros odio et odio.</p>
    <p style="margin-top:16px">Aliquam mollis mi a ornare congue. Ut vel purus fermentum, accumsan orci ullamcorper, ullamcorper tortor.</p>
  </div>
  <div class="pager">
    <span><svg width="12" height="16" viewBox="0 0 12 16"><path d="M9 2L3 8l6 6" fill="none" stroke="#fff" stroke-width="2"/></svg></span>
    <span><svg width="12" height="16" viewBox="0 0 12 16"><path d="M3 2l6 6-6 6" fill="none" stroke="#fff" stroke-width="2"/></svg></span>
    <em>View More page examples</em>
  </div>
</section>

<section class="section testimonials">
  <h2>Testimonials</h2>
  <svg class="chev" style="left:130px" width="16" height="30" viewBox="0 0 16 30"><path d="M14 2L2 15l12 13" fill="none" stroke="#444" stroke-width="2"/></svg>
  <div class="video" role="img" aria-label="Video still of a smiling customer giving a testimonial"><span class="play"></span></div>
  <svg class="chev" style="left:642px" width="16" height="30" viewBox="0 0 16 30"><path d="M2 2l12 13L2 28" fill="none" stroke="#444" stroke-width="2"/></svg>
  <p class="quote">"Buying more dedicated servers to scale our databases quickly gets expensive. Stackhaven Cloud Databases solves that: we can have the same features and performance, without adding cost."</p>
  <p class="who"><strong>RK Vandermolen</strong><br>CTO, PageLoom</p>

  <div class="fan">
    <div class="fan-head"><span class="fan-sq"></span><div><b>Get Fan Exclusives</b><span>Like us on Circlepage</span></div></div>
    <div class="fan-box">
      <div class="fan-row"><span>Meridale Transfers</span><span class="fan-like">Like</span><span>Meridale Transfers</span></div>
      <p class="fan-count">226,327 people like this</p>
      <div class="fan-grid" role="img" aria-label="Grid of follower profile photos"></div>
    </div>
    <p class="fan-foot">Circlepage social plugin</p>
  </div>
</section>

<section class="section contact">
  <h2>CONTACT US</h2>
  <p>Praesent quis mauris risus. Suspendisse ac eros pulvinar, euismod arcu vitae, convallis enim. Vivamus diam erat, commodo quis cursus fermentum, posuere non nisi. Integer egestas a sapien sit amet dignissim.</p>
</section>

<section class="section map" role="img" aria-label="Street map of the city centre showing the office location">
  <div class="zoom" style="top:48px">+</div>
  <div class="zoom" style="top:103px">&minus;</div>
  <svg class="abs" style="left:565px;top:243px" width="72" height="100" viewBox="0 0 72 100"><path d="M36 2C17 2 2 17 2 36c0 26 34 62 34 62s34-36 34-62C70 17 55 2 36 2z" fill="#0c2b5e"/><circle cx="36" cy="36" r="22" fill="none" stroke="#fff" stroke-width="3"/></svg>
</section>

<section class="section clients">
  <h3><span>Some Of Our Clients</span></h3>
  <div class="client-row">
    <div class="client">Aldane</div>
    <div class="client">Verona</div>
    <div class="client">Hollis Medical</div>
    <div class="client">Tunewell</div>
    <div class="client">Coldarc</div>
    <div class="client">Ferris</div>
    <div class="client">Marsh Realty</div>
  </div>
</section>

<footer class="section footer">
  <div class="fcol" style="left:100px"><h4>BUSINESS</h4><ul><li>Why us</li><li>Payment options</li><li>How it works</li><li>Merchant FAQs</li></ul></div>
  <div class="fcol" style="left:261px"><h4>SERVICES</h4><ul><li>Why Meridale Transfers</li><li>How it works</li><li>Payment gatway</li><li>Support</li><li>Live demo</li></ul></div>
  <div class="fcol" style="left:486px"><h4>FIND US ON</h4><div class="social"><span></span><span></span><span></span><span></span></div></div>
  <div class="fcol news" style="left:762px"><h4>Subscribe newsletter</h4><form><input value="enter your mail address"><button type="button">submit</button></form></div>
  <p class="copy">Copyright 2014 Meridale Transfers. All rights are reserved.</p>
</footer>

</body>
</html>
```